Bioidentical Hormone Replacement Therapy

I need a rectangular brochure- sized flyer (one page) designed to hand out to patients that will capture their attention. The flyer will display our company name, logo, contact information, website and social media information provided below. We need people to know that we offer a personalized approach to medicine. The main purpose of the flyer is to convey the fact that we offer bioidentical hormone replacement therapy (BHRT) for women and men by a pellet insertion procedure even for non members. Symptoms this can help with are for Women:
Fatigue*
Trouble sleeping*
Irritability*
Anxiousness*
Mood swings*
Low mood*
Night sweats*
Hot flashes or flushes*
Weight gain*
Decreased sex drive*
Discomfort during intercourse*
Low bone density*
and for Men:
Low sex drive*
Increased body fat
(especially in the waist area)*
Loss of muscle mass and strength*
Reduced mental focus*
Feelings of anxiety*
Irritability*
Fatigue*
Elevated blood sugar*
High cholesterol*
Practice name: Brookhaven Internal Medicine
Address: 4382 Larkspur Lane, Columbia, SC. 20917
Phone: 803-671-5394
Email: jtrevor@brookhavenimd.example
Website: https://brookhavenimd.example
Facebook: https://www.facebook.com/profile.php?id=70938265147723
Updates
For sizing 3.5 inch or so by 8.5 inch or so inch is fine. Not sure what is standard printing paper size for flyer.
Target Market(s)
Medical Patients
Industry/Entity Type
Healthcare
Look and feel

```html
<!DOCTYPE html>
<html lang="en">
<head>
<meta charset="utf-8">
<title>BHRT – Brookhaven Internal Medicine</title>
<link href="https://fonts.googleapis.com/css2?family=Roboto:wght@700;900&family=Roboto+Condensed:wght@300;400;700&display=swap" rel="stylesheet">
<style>
  :root {
    --brand-blue: #1757a6;
    --navy: #1b2c57;
    --ink: #3a3a3a;
    --white: #ffffff;
    --label-bg: rgba(255, 255, 255, 0.82);
    --sand-top: #8fa6b0;
    --sand-mid: #b9a58a;
    --sand-bottom: #d8c4a4;
    --sky-top: #4f8fd6;
    --sky-mid: #9cc3ea;
    --rock: #3d4a2c;
  }
  * { margin: 0; padding: 0; box-sizing: border-box; }
  html, body { width: 1200px; height: 2914px; overflow: hidden; background: var(--white); }
  .flyer {
    position: relative;
    width: 1200px;
    height: 2914px;
    overflow: hidden;
    font-family: "Roboto Condensed", "Arial Narrow", sans-serif;
    color: var(--ink);
  }

  /* Photo areas */
  .photo { position: absolute; top: 0; height: 2514px; }
  .photo--women {
    left: 0; width: 599px;
    background: linear-gradient(180deg, var(--sand-top) 0%, #a9b5b3 35%, var(--sand-mid) 60%, var(--sand-bottom) 100%);
  }
  .photo--men {
    left: 601px; width: 599px;
    background: linear-gradient(180deg, var(--sky-top) 0%, var(--sky-mid) 45%, #b9d4ef 70%, var(--rock) 100%);
  }
  .divider { position: absolute; left: 599px; top: 0; width: 2px; height: 2514px; background: rgba(255,255,255,0.7); }

  .header-shape { position: absolute; left: 0; top: 0; width: 1200px; height: 760px; }

  /* Logo */
  .logo {
    position: absolute; left: 62px; top: 23px;
    width: 434px; height: 434px;
    border: 4px solid var(--navy);
    border-radius: 50%;
    display: flex; align-items: center; justify-content: center;
    text-align: center;
  }
  .logo__name {
    font-family: "Roboto Condensed", sans-serif;
    font-weight: 400;
    font-size: 50px;
    line-height: 1.1;
    letter-spacing: 2px;
    text-transform: uppercase;
    color: var(--navy);
  }

  /* Heading */
  .title {
    position: absolute; left: 552px; top: 110px;
    font-family: "Roboto", sans-serif;
    font-weight: 900;
    font-size: 210px;
    line-height: 1;
    letter-spacing: 4px;
    color: var(--brand-blue);
  }
  .subtitle {
    position: absolute; left: 556px; top: 318px;
    font-family: "Roboto Condensed", sans-serif;
    font-weight: 300;
    font-size: 72px;
    line-height: 1.08;
    color: var(--ink);
  }

  /* Symptom lists */
  .symptoms {
    position: absolute; top: 870px;
    list-style: none;
    display: flex; flex-direction: column; gap: 36px;
    width: 504px;
  }
  .symptoms--women { left: 64px; }
  .symptoms--men { left: 631px; }
  .symptom {
    background: var(--label-bg);
    min-height: 91px;
    display: flex; align-items: center;
    font-weight: 300;
    font-size: 45px;
    line-height: 1.0;
  }
  .symptoms--women .symptom {
    padding: 8px 70px 8px 32px;
    clip-path: polygon(0 0, 88% 0, 100% 50%, 88% 100%, 0 100%);
  }
  .symptoms--men .symptom {
    padding: 8px 32px 8px 70px;
    justify-content: flex-end;
    text-align: right;
    clip-path: polygon(12% 0, 100% 0, 100% 100%, 12% 100%, 0 50%);
  }
  .symptom--tall { min-height: 244px; }
  .symptom--double { min-height: 114px; }

  /* Footer */
  .footer {
    position: absolute; left: 0; top: 2514px;
    width: 1200px; height: 400px;
    background: var(--brand-blue);
    color: var(--white);
    display: flex; flex-direction: column; align-items: center; justify-content: center;
    gap: 28px;
  }
  .footer__phone {
    display: flex; align-items: center; gap: 30px;
    font-family: "Roboto Condensed", sans-serif;
    font-weight: 700;
    font-size: 104px;
    line-height: 1;
  }
  .footer__icon { width: 68px; height: 68px; }
  .footer__web {
    font-family: "Roboto", sans-serif;
    font-weight: 700;
    font-size: 62px;
    letter-spacing: 3px;
    line-height: 1;
  }
</style>
</head>
<body>
<main class="flyer">
  <div class="photo photo--women" role="img" aria-label="Photo of a woman in a white dress walking along a sandy beach by the sea"></div>
  <div class="photo photo--men" role="img" aria-label="Photo of a man in a yellow jacket standing on a rock with arms open under a blue sky"></div>
  <div class="divider"></div>

  <svg class="header-shape" viewBox="0 0 1200 760" aria-hidden="true">
    <polygon points="0,0 1200,0 1200,458 600,754 0,458" fill="#ffffff"/>
  </svg>

  <div class="logo">
    <span class="logo__name">Brookhaven<br>Internal<br>Medicine</span>
  </div>

  <h1 class="title">BHRT</h1>
  <p class="subtitle">Symptoms this can<br>help with are:</p>

  <ul class="symptoms symptoms--women" aria-label="Symptoms for women">
    <li class="symptom">Fatigue</li>
    <li class="symptom">Trouble sleeping</li>
    <li class="symptom">Irritability</li>
    <li class="symptom">Anxiousness</li>
    <li class="symptom">Mood swings</li>
    <li class="symptom">Low mood</li>
    <li class="symptom">Night sweats</li>
    <li class="symptom">Hot flashes or flushes</li>
    <li class="symptom">Weight gain</li>
    <li class="symptom">Decreased sex drive</li>
    <li class="symptom symptom--double">Discomfort during intercourse</li>
    <li class="symptom">Low bone density</li>
  </ul>

  <ul class="symptoms symptoms--men" aria-label="Symptoms for men">
    <li class="symptom">Low sex drive</li>
    <li class="symptom symptom--tall">Increased body fat (especially in the waist area)</li>
    <li class="symptom symptom--double">Loss of muscle mass and strength</li>
    <li class="symptom">Reduced mental focus</li>
    <li class="symptom">Feelings of anxiety</li>
    <li class="symptom">Irritability</li>
    <li class="symptom">Fatigue</li>
    <li class="symptom">Elevated blood sugar</li>
    <li class="symptom">High cholesterol</li>
  </ul>

  <footer class="footer">
    <div class="footer__phone">
      <svg class="footer__icon" viewBox="0 0 24 24" aria-hidden="true">
        <circle cx="12" cy="12" r="10.5" fill="none" stroke="#fff" stroke-width="2"/>
        <path d="M8.2 6.5l1.8-.4 1.2 2.8-1.3 1c.6 1.4 1.6 2.5 3 3.2l1-1.3 2.8 1.2-.4 1.8c-.2.6-.8 1-1.5.9-4-.6-7.2-3.8-7.6-7.8 0-.6.4-1.2 1-1.4z" fill="#fff"/>
      </svg>
      <span>803-671-5394</span>
    </div>
    <div class="footer__web">WWW.BROOKHAVENIMD.EXAMPLE</div>
  </footer>
</main>
</body>
</html>
```